Website/Logo Design

We need a logo and website design for an opinion mining startup called VantaLume. Our technology mines the web to automatically discover what people are saying about brands, products, etc. The project we are fielding here is for our informational, public-facing website. In its initial incarnation, it will simply be a vehicle for marketing materials and information on our company and its offerings, but it should be flexible enough to expand as more content/functionality is added.

Some designs we like are:
http://www.tradewhisk.example
http://www.gorvantel.example
http://www.kfz.example
http://www.lintwharf.example
http://moxbarrel.example
http://trundlemq.example
http://www.zopla.example
Updates

All, please try to shy away from using a photo of a person as the focal point of the design.  Our company is more technological than social.

Target Market(s)

Primarily businesses interested in sentiment analysis (typically companies involved in advertising, market research, PR, etc.)

Industry/Entity Type

It Company

Requirements
Must have
• We are looking for a clean, modern, and professional design. This includes a logo, homepage, and internal page if it will differ from the homepage.
Nice to have
• It would be excellent if you could provide an HTML mockup if your design is chosen.
Should not have
• Flash, excessive bells and whistles

```html
<!DOCTYPE html>
<html lang="en">
<head>
<meta charset="utf-8">
<title>VantaLume — Opinion Mining</title>
<link rel="stylesheet" href="https://fonts.googleapis.com/css2?family=Arimo:wght@400;700&family=Noto+Sans:wght@400;700&family=Tinos&display=swap">
<style>
:root{
  --sky-top:#e4f4fd;
  --sky-bottom:#bfe4f6;
  --teal:#13768c;
  --teal-deep:#0e5666;
  --nav-top:#12788d;
  --nav-bottom:#073e4c;
  --ink:#1f1f1f;
  --panel:#e8e6e7;
  --footer:#231f20;
  --white:#ffffff;
  --muted:#8c8c8c;
  --alert:#e00000;
}
*{margin:0;padding:0;box-sizing:border-box}
html,body{width:1200px;height:1188px;overflow:hidden;background:var(--white)}
body{position:relative;font-family:"Noto Sans",sans-serif;color:var(--ink)}
.site-header{position:absolute;left:0;top:0;width:1200px;height:186px;background:linear-gradient(var(--sky-top),var(--sky-bottom))}
.brand{position:absolute;left:58px;top:54px;font-family:"Arimo",sans-serif;font-weight:700;font-size:62px;letter-spacing:-1px;color:var(--ink)}
.call{position:absolute;right:55px;top:10px;text-align:right}
.call-label{font-family:"Arimo",sans-serif;font-weight:700;font-size:23px;color:var(--teal);letter-spacing:.5px}
.call-number{font-family:"Noto Sans",sans-serif;font-size:21px;color:var(--ink);margin-top:-2px}
.login{position:absolute;left:821px;top:76px;width:330px;font-family:"Noto Sans",sans-serif}
.login-title{font-size:16px;margin-bottom:8px}
.login-fields{display:flex;gap:12px}
.field{width:156px;height:25px;border:1px solid #a8b4bb;background:var(--white);font-size:12px;color:#777;padding:4px 6px}
.login-actions{display:flex;align-items:center;margin-top:16px;font-size:13px;font-weight:700;white-space:nowrap}
.btn-login{width:53px;height:25px;background:#7bbfd6;border:1px solid #3f7f93;font-size:12px;font-weight:400;display:flex;align-items:center;justify-content:center;margin-right:9px}
.forgot{text-decoration:underline;color:#000}
.new{color:var(--alert);margin-left:4px}
.nav{position:absolute;left:0;top:186px;width:1200px;height:54px;background:linear-gradient(var(--nav-top),var(--nav-bottom));display:flex;justify-content:center;align-items:center;font-family:"Arimo",sans-serif;font-size:19px;color:var(--white)}
.nav span.sep{margin:0 40px}
.hero{position:absolute;left:0;top:240px;width:1200px;height:337px;background:var(--white)}
.hero-art{position:absolute;left:130px;top:10px;width:278px;height:327px;background:linear-gradient(135deg,#f3f3f3 0%,#e7f0f5 40%,#f4d9c5 70%,#f6f6f6 100%)}
.hero-text{position:absolute;left:405px;top:100px;width:675px;text-align:center;font-family:"Noto Sans",sans-serif;font-size:30px;line-height:43px;color:var(--teal-deep)}
.content{position:absolute;left:0;top:577px;width:1200px;height:476px;background:var(--panel)}
.block{position:absolute;width:534px}
.block.right{width:509px}
.block h2{font-family:"Arimo",sans-serif;font-weight:700;font-size:18px;color:var(--ink);padding-left:2px;height:30px;display:flex;align-items:baseline}
.block h2 em{font-style:normal;font-size:26px;color:var(--teal);margin-left:6px}
.dots{border-top:2px dotted #777;margin-top:4px}
.block p{font-size:12.5px;line-height:21.5px;margin-top:10px;color:#111}
.more{display:flex;align-items:center;margin-top:22px;font-size:13px;font-weight:700}
.more svg{margin-right:5px}
.clients{margin-top:18px;height:100px;background:var(--white);display:grid;grid-template-columns:repeat(4,1fr);align-items:center;justify-items:center;padding:6px 4px}
.clients span{font-family:"Arimo",sans-serif;font-weight:700;font-size:17px;color:var(--muted);white-space:nowrap}
.footer{position:absolute;left:0;top:1053px;width:1200px;height:135px;background:var(--footer);color:var(--white)}
.foot-brand{position:absolute;left:58px;top:14px;font-family:"Tinos",serif;font-size:27px;color:var(--teal)}
.foot-address{position:absolute;left:64px;top:52px;font-family:"Arimo",sans-serif;font-size:15px;line-height:18px}
.foot-rule{position:absolute;left:226px;top:10px;height:115px;border-left:2px dotted #666}
.foot-contact{position:absolute;left:253px;top:50px;font-family:"Arimo",sans-serif;font-size:13.5px;font-weight:700;line-height:16px}
.foot-contact b{color:var(--teal)}
.foot-links{position:absolute;right:55px;top:52px;text-align:right;font-family:"Noto Sans",sans-serif;font-size:12.5px;white-space:nowrap}
.foot-links .sep{margin:0 8px}
.copy{margin-top:6px}
</style>
</head>
<body>
<header class="site-header">
  <div class="brand">VantaLume</div>
  <div class="call">
    <div class="call-label">CALL US</div>
    <div class="call-number">Tel : +33(0)6 412 730.55</div>
  </div>
  <div class="login">
    <div class="login-title">Log&nbsp; In</div>
    <div class="login-fields">
      <div class="field">user name</div>
      <div class="field">password</div>
    </div>
    <div class="login-actions">
      <div class="btn-login">Log In</div>
      <span class="forgot">forgot your password</span>&nbsp;?<span class="new">New ?</span>&nbsp;Sign Up
    </div>
  </div>
</header>
<nav class="nav">
  <span>Home</span><span class="sep">|</span>
  <span>About VantaLume</span><span class="sep">|</span>
  <span>How We Work</span><span class="sep">|</span>
  <span>Case Studies</span><span class="sep">|</span>
  <span>Pricing</span><span class="sep">|</span>
  <span>Contact</span>
</nav>
<section class="hero">
  <div class="hero-art" role="img" aria-label="Glossy 3D bar chart illustration in red, orange, blue and green"></div>
  <p class="hero-text">Our technology mines the web to automatically discover what people are saying about brands, products, etc.</p>
</section>
<main class="content">
  <div class="block" style="left:56px;top:28px">
    <h2>Welcome to<em>VantaLume</em></h2>
    <div class="dots"></div>
    <p>Lorem ipsum dolor sit amet, consectetur adipiscing elit. Maecenas luctus arcu sit amet quam viverra condimentum. Suspendisse aliquam ullamcorper sapien suscipit laoreet. Suspendisse varius sodales lectus sit amet convallis. Vestibulum facilisis condimentum lorem, quis commodo tortor luctus eget.</p>
    <div class="more"><svg width="11" height="11"><rect width="11" height="11" fill="#13768c"/><path d="M3 3l5 5M8 4v4H4" stroke="#fff" stroke-width="1.4" fill="none"/></svg>read more</div>
  </div>
  <div class="block right" style="left:636px;top:28px">
    <h2>our<em>Services</em></h2>
    <div class="dots"></div>
    <p>Lorem ipsum dolor sit amet, consectetur adipiscing elit. Maecenas luctus arcu sit amet quam viverra condimentum. Suspendisse aliquam ullamcorper sapien suscipit laoreet. Suspendisse varius sodales lectus sit amet convallis. Vestibulum facilisis condimentum lorem, quis commodo tortor luctus eget.</p>
    <div class="more"><svg width="11" height="11"><rect width="11" height="11" fill="#13768c"/><path d="M3 3l5 5M8 4v4H4" stroke="#fff" stroke-width="1.4" fill="none"/></svg>read more</div>
  </div>
  <div class="block" style="left:56px;top:238px">
    <h2>Who<em>We Are</em></h2>
    <div class="dots"></div>
    <p>Lorem ipsum dolor sit amet, consectetur adipiscing elit. Maecenas luctus arcu sit amet quam viverra condimentum. Suspendisse aliquam ullamcorper sapien suscipit laoreet. Suspendisse varius sodales lectus sit amet convallis. Vestibulum facilisis condimentum lorem, quis commodo tortor luctus eget.</p>
    <div class="more"><svg width="11" height="11"><rect width="11" height="11" fill="#13768c"/><path d="M3 3l5 5M8 4v4H4" stroke="#fff" stroke-width="1.4" fill="none"/></svg>read more</div>
  </div>
  <div class="block right" style="left:636px;top:238px">
    <h2>our<em>Clients</em></h2>
    <div class="dots"></div>
    <div class="clients">
      <span>Pellax</span><span>Quorvis</span><span>Draymont</span><span>Kestrio</span>
      <span>Lumbrex</span><span>Fallow Ridge</span><span>Qelvorn</span><span>Harwick Olsen</span>
    </div>
  </div>
</main>
<footer class="footer">
  <div class="foot-brand">VantaLume</div>
  <div class="foot-address">17 dummy address<br>Dummy Address<br>Dummy Addrses</div>
  <div class="foot-rule"></div>
  <div class="foot-contact">
    <b>Tel :</b> +33(0)6 41 27 30 55<br>
    <b>Email :</b> hello@vantalume.example<br>
    <b>Skype :</b> lena.morrow
  </div>
  <div class="foot-links">
    <div>Home<span class="sep">|</span>About VantaLume<span class="sep">|</span>How We Work<span class="sep">|</span>Case Studies<span class="sep">|</span>Pricing<span class="sep">|</span>Clients<span class="sep">|</span>Blogs<span class="sep">|</span>Contact Us</div>
    <div class="copy">© 2010 vantalume.example | All rights reserved</div>
  </div>
</footer>
</body>
</html>
```